Guitar teacher and Composer needs a Business Card design

I am looking for a designer who would like to implement the general idea of the design which I am providing with a draft in the uploaded file called Tomas.png. Please feel free to add your own creative touch to my idea.
There should definitely be an abstract image of a guitar on the business card. The colours to use - black and white, could be also grey. Which one to use as the main colour - to your decision. You can try to make it half-half, for example black part with guitar and the rest - white or the other way round. Would be cool to see there some element standing out in red, such as some note, or one or all strings of the guitar, or the line of the contour of the guitar for example..
It would also be nice to see a "reverse" version where the background would be black and the strings and contour of the guitar would be white etc.
Thanks to everyone who is going to participate in this design project!
Target Market(s)
potential students and customers
Industry/Entity Type
Teacher
Contact Information for Business Card
see "Project description"
Requirements
Must have
- I want to have an ABSTRACT image of a CLASSICAL guitar or part of it. It can be just the contour of it or just a few lines giving a hint about it or so.
Nice to have
- Would be good to have some small element standing out in red. Like some little detail, or one line, or icons of contacts, or string(s) of the guitar, or a note.......
Should not have
- I DON'T want to have a PHOTO of a guitar on my business card. And i DON'T need an image of an E-GUITAR.
- I don't want the words "Phone", "E-Mail", "Website", or "Address" to appear on the business card but rather have icons/symbols for that, as shown in my draft.

```html
<!DOCTYPE html>
<html lang="de">
<head>
<meta charset="utf-8">
<title>Tomas Valenko – Visitenkarte</title>
<link rel="stylesheet" href="https://fonts.googleapis.com/css2?family=Arimo&family=Tinos&display=swap">
<style>
  :root {
    --page-bg: #d9d6d1;
    --card-black: #0b0b0c;
    --card-grey: #38393b;
    --accent-red: #e0262b;
    --text-white: #f2f2f2;
    --text-soft: #dcdcdc;
    --wood-light: #e2b885;
    --wood-dark: #a8683a;
  }
  * { margin: 0; padding: 0; box-sizing: border-box; }
  html, body {
    width: 1200px; height: 886px; overflow: hidden;
    background: var(--page-bg);
  }
  .card {
    position: absolute; left: 100px; top: 153px;
    width: 1000px; height: 580px; border-radius: 34px; overflow: hidden;
    background:
      linear-gradient(115deg, var(--card-black) 0%, var(--card-black) 30%, var(--card-grey) 42%, #1a1a1b 56%, var(--card-black) 80%);
    box-shadow: 0 12px 30px rgba(0,0,0,.35);
    font-family: "Arimo", Arial, sans-serif;
  }
  .roles {
    position: absolute; left: 64px; top: 60px;
    list-style: none; color: var(--accent-red);
    font-size: 30px; line-height: 42px;
  }
  .name {
    position: absolute; right: 240px; top: 92px;
    font-family: "Tinos", "Times New Roman", serif; font-weight: 400;
    font-size: 46px; letter-spacing: 2px; color: var(--text-white);
  }
  .contacts {
    position: absolute; right: 230px; top: 292px;
    list-style: none; text-align: right; color: var(--text-soft);
    font-size: 26px; line-height: 46px;
  }
  .contacts li { display: flex; justify-content: flex-end; align-items: center; gap: 14px; }
  .contacts svg { width: 22px; height: 22px; fill: var(--accent-red); flex: none; }
  .guitar {
    position: absolute; right: 34px; top: 22px;
    width: 160px; height: 536px; border-radius: 60px 60px 80px 80px;
    background: linear-gradient(180deg, #5a3a2a 0%, #5a3a2a 52%, var(--wood-light) 62%, var(--wood-dark) 100%);
  }
</style>
</head>
<body>
  <article class="card">
    <ul class="roles">
      <li>Gitarrenlehrer</li>
      <li>Komponist</li>
      <li>Arrangevr</li>
    </ul>

    <h1 class="name">TOMAS VALENKO</h1>

    <ul class="contacts">
      <li>+49 170 555 012 34
        <svg viewBox="0 0 24 24"><rect x="1" y="1" width="22" height="22" rx="4"/><path d="M7 6c1 5 4 9 11 12l1.5-2.5-3-2-1.5 1.5c-2-1-4-3-5-5l1.5-1.5-2-3z" fill="#0b0b0c"/></svg>
      </li>
      <li>tomas@saitenklang.de
        <svg viewBox="0 0 24 24"><rect x="1" y="1" width="22" height="22" rx="4"/><path d="M5 8h14v9H5z M5 8l7 5 7-5" fill="none" stroke="#0b0b0c" stroke-width="1.6"/></svg>
      </li>
      <li>www.saitenklang.de
        <svg viewBox="0 0 24 24"><circle cx="12" cy="12" r="11"/><path d="M1 12h22M12 1v22M4 6h16M4 18h16M12 1c-5 5-5 17 0 22M12 1c5 5 5 17 0 22" fill="none" stroke="#0b0b0c" stroke-width="1.2"/></svg>
      </li>
      <li>Lindenweg 27, Musterstadt 80123,
        <svg viewBox="0 0 24 24"><path d="M12 1a8 8 0 0 0-8 8c0 6 8 14 8 14s8-8 8-14a8 8 0 0 0-8-8z"/><circle cx="12" cy="9" r="3" fill="#0b0b0c"/></svg>
      </li>
    </ul>

    <div class="guitar" role="img" aria-label="Klassische Gitarre, senkrecht stehend, Kopf oben, heller Holzkorpus unten"></div>
  </article>
</body>
</html>
```